A4 Simple eye catching special offers page with minimal text

I would like an A4 page to advertise my special offers on for sale sign boards. I want my logo on the design and maybe some pictures i have attached, or maybe a design without the pictures i might like the design with or without them. The following text should be used:
Free boards
Free rebrand
Read on to find out more

Target Market(s)

Businesses

Industry/Entity Type

Real Estate Agent

Requirements
Must have
• good design
Nice to have
• eye catching

```html
<!DOCTYPE html>
<html lang="en">
<head>
<meta charset="utf-8">
<title>Free Boards, Free Rebrand – Special Offer</title>
<link href="https://fonts.googleapis.com/css2?family=Figtree:wght@500;600;700;800&family=Arimo:wght@400&display=swap" rel="stylesheet">
<style>
  :root {
    --navy: #2b2a55;
    --navy-deep: #2a2950;
    --red: #e3242e;
    --coral: #ff4a5a;
    --grey-text: #9a9a9c;
    --grey-edge: #e6e8e8;
    --paper: #ffffff;
    --backdrop: #d9d9de;
  }
  * { margin: 0; padding: 0; box-sizing: border-box; }
  html, body {
    width: 1200px;
    height: 1196px;
    overflow: hidden;
    background: var(--backdrop);
  }
  .canvas {
    position: relative;
    width: 1200px;
    height: 1196px;
    overflow: hidden;
  }
  .flyer {
    position: absolute;
    left: 180px;
    top: 6px;
    width: 903px;
    height: 1273px;
    background: var(--paper);
    transform: scale(0.9301);
    transform-origin: top left;
    overflow: hidden;
    font-family: "Figtree", "Helvetica Neue", Arial, sans-serif;
  }
  .flyer__graphics {
    position: absolute;
    inset: 0;
    width: 903px;
    height: 1273px;
  }
  .offer {
    position: absolute;
    left: 183px;
    top: 650px;
    color: var(--navy-deep);
  }
  .offer__intro,
  .offer__outro {
    font-size: 31px;
    font-weight: 600;
    color: var(--grey-text);
    letter-spacing: 0.2px;
  }
  .offer__list { list-style: none; margin: 8px 0 6px; }
  .offer__item {
    position: relative;
    font-size: 80px;
    font-weight: 700;
    line-height: 106px;
    letter-spacing: -0.5px;
  }
  .offer__tick {
    position: absolute;
    left: -115px;
    top: 20px;
    width: 82px;
    height: 76px;
  }
  .footer__web {
    position: absolute;
    left: 58px;
    top: 1181px;
    width: 253px;
    height: 53px;
    border: 3px solid var(--red);
    background: var(--navy);
    color: #fff;
    font-weight: 700;
    font-size: 18px;
    display: flex;
    align-items: center;
    justify-content: center;
  }
  .footer__contact {
    position: absolute;
    top: 1191px;
    font-family: "Arimo", Arial, sans-serif;
    font-size: 13.5px;
    line-height: 16px;
    color: var(--navy);
  }
  .footer__address { left: 355px; }
  .footer__direct { left: 678px; }
  .footer__divider {
    position: absolute;
    left: 654px;
    top: 1193px;
    width: 2px;
    height: 30px;
    background: var(--red);
  }
</style>
</head>
<body>
<div class="canvas">
  <article class="flyer">
    <svg class="flyer__graphics" viewBox="0 0 903 1273" aria-hidden="false">
      <defs>
        <linearGradient id="signsTone" x1="0" y1="1" x2="1" y2="0">
          <stop offset="0" stop-color="#d9402c"/>
          <stop offset="0.25" stop-color="#2aa3b8"/>
          <stop offset="0.5" stop-color="#e8c43a"/>
          <stop offset="0.7" stop-color="#c9d43a"/>
          <stop offset="1" stop-color="#4a2a78"/>
        </linearGradient>
      </defs>
      <rect class="header__base" x="0" y="0" width="903" height="520" fill="var(--navy)"/>
      <rect class="header__photo" x="0" y="85" width="760" height="420" fill="url(#signsTone)"
            role="img" aria-label="Photograph of a row of colourful estate agent for-sale signboards"/>
      <rect class="header__photo" x="300" y="0" width="460" height="90" fill="#4b2a7a"
            role="img" aria-label="Upper part of the signboards photograph"/>
      <polygon class="header__band" points="355,330 903,190 903,315 355,440" fill="var(--red)"/>
      <polygon class="header__band" points="550,265 903,205 903,260 550,320" fill="var(--coral)" opacity="0.85"/>
      <polygon class="header__band" points="440,385 820,310 820,345 440,420" fill="#ff6b86" opacity="0.5"/>
      <polygon class="header__edge" points="0,493 623,372 903,497 903,1273 0,1273" fill="var(--grey-edge)"/>
      <polygon class="page__body" points="0,510 623,392 903,518 903,1273 0,1273" fill="var(--paper)"/>
      <polygon class="footer__stripe" points="0,1090 292,1273 0,1273" fill="var(--red)"/>
      <polygon class="footer__corner" points="0,1120 200,1273 0,1273" fill="var(--navy)"/>
    </svg>

    <section class="offer">
      <p class="offer__intro">switch to us and get</p>
      <ul class="offer__list">
        <li class="offer__item">
          <svg class="offer__tick" viewBox="0 0 82 76" aria-hidden="true"><path d="M2 44 C10 40 16 42 22 58 C36 30 56 10 80 0 C58 18 40 44 26 74 C20 62 12 50 2 44 Z" fill="var(--red)"/></svg>
          FREE BOARDS
        </li>
        <li class="offer__item">
          <svg class="offer__tick" viewBox="0 0 82 76" aria-hidden="true"><path d="M2 44 C10 40 16 42 22 58 C36 30 56 10 80 0 C58 18 40 44 26 74 C20 62 12 50 2 44 Z" fill="var(--red)"/></svg>
          FREE REBRAND
        </li>
      </ul>
      <p class="offer__outro">read on to find out more</p>
    </section>

    <footer class="footer">
      <div class="footer__web">www.BoardWise.co.uk</div>
      <p class="footer__contact footer__address">Unit 14, Mill Lane Business Park<br>Mill Lane, Northwich, Cheshire, CW9 7QT</p>
      <span class="footer__divider"></span>
      <p class="footer__contact footer__direct">0333 4418207<br>info@boardwise.co.uk</p>
    </footer>
  </article>
</div>
</body>
</html>
```